Web design - holistic filmmaker

I need a design for my new website.

I am a holistic filmmaker, ie I make films for healers, alternative practitioners, spiritual people and institutions that offer training in this field.

The design should be noble, bright, convey the feeling of space and expanse and have some particularly beautiful color accents.

The structure is: start page, offer, references, about me, imprint.

As an idea for the start page, I thought that either I could introduce myself as a filmmaker and my offer, or we could start right on the start page with the references, ie photos and links to already realized projects.

If you want more information or an exchange, I'd love to hear from you. At the moment I just don't know how to describe it better.

The winner will then be asked to design a logo.

Target Market(s)

healers, alternative practitioners, spiritual people and institutions that offer training in this field

Industry/Entity Type

Film production

Number of Pages Required

3 page

```html
<!DOCTYPE html>
<html lang="en">
<head>
<meta charset="utf-8">
<title>Lena Marwitz – Films for the mindful seekers</title>
<link href="https://fonts.googleapis.com/css2?family=Poppins:wght@300;400;500;600;700;800&display=swap" rel="stylesheet">
<style>
:root{
  --pink:#ff3366;
  --blue:#3325b0;
  --ink:#1f1f2b;
  --text:#555566;
  --muted:#8a8a99;
  --pale:#f2f2f7;
  --white:#ffffff;
}
*{box-sizing:border-box;margin:0;padding:0}
html,body{width:1200px;height:3573px;overflow:hidden}
body{position:relative;font-family:'Poppins',sans-serif;color:var(--ink);background:var(--white)}
.abs{position:absolute}
.btn{position:absolute;display:flex;align-items:center;justify-content:center;background:var(--pink);color:var(--white);font-weight:600;text-transform:uppercase;border-radius:40px;text-decoration:none}

.site-header{position:absolute;left:0;top:0;width:1200px;height:129px}
.brand{position:absolute;display:flex;align-items:center;gap:14px}
.brand-mark{width:58px;height:58px;border-radius:50%;background:var(--blue)}
.brand-name{font-size:48px;font-weight:400;color:var(--ink);line-height:1}
.brand-tag{font-size:18px;color:var(--blue);margin-top:6px}
.main-nav{position:absolute;top:47px;left:600px;display:flex;gap:29px;font-size:20px}
.main-nav a{color:var(--ink);text-decoration:none}
.main-nav a.active{color:var(--pink)}

.hero{position:absolute;left:0;top:129px;width:1200px;height:631px;overflow:hidden;
  background:linear-gradient(100deg,#4a2a9a 0%,#6a2a86 40%,#8a2c6a 70%,#5a2a8f 100%)}
.hero-title{position:absolute;left:108px;top:292px;font-size:82px;font-weight:700;line-height:.95;color:var(--white);letter-spacing:-.5px}
.hero .btn{left:111px;top:486px;width:243px;height:66px;font-size:19px}

.kicker{position:absolute;width:1200px;text-align:center;color:var(--blue);font-size:24px;font-weight:400}
.heading{position:absolute;width:1200px;text-align:center;font-size:45px;font-weight:700;color:var(--ink)}

.process-line{position:absolute;left:111px;top:1062px;width:971px;height:4px;background:var(--blue)}
.dot{position:absolute;width:14px;height:14px;border-radius:50%;background:var(--blue);top:1057px}
.step{position:absolute;top:980px;width:250px;text-align:center}
.step-icon{width:168px;height:168px;margin:0 auto;border-radius:50%;background:var(--white);box-shadow:0 4px 14px rgba(0,0,0,.12);display:flex;align-items:center;justify-content:center}
.step-num{margin-top:28px;color:var(--pink);font-size:17px}
.step-name{font-size:23px;font-weight:500;margin-top:4px}
.step-text{font-size:17px;color:var(--muted);line-height:25px;margin-top:12px;font-weight:300}

.about{position:absolute;left:0;top:1375px;width:1200px;height:560px;background:var(--pale);overflow:hidden}
.about-photo{position:absolute;left:0;top:0;width:656px;height:560px;background:linear-gradient(135deg,#6a6a6a,#2a2a2a)}
.about-body{position:absolute;left:673px;top:57px;width:440px}
.about-body .kicker-left{color:var(--blue);font-size:24px}
.about-body h2{font-size:44px;font-weight:700;margin-top:4px}
.about-body p{font-size:16px;color:var(--text);line-height:27.5px;margin-top:18px;font-weight:300}
.about .btn{left:674px;top:442px;width:153px;height:55px;font-size:17px}

.thumb{position:absolute;overflow:hidden}
.play{position:absolute;left:50%;top:50%;width:64px;height:64px;margin:-32px 0 0 -32px;border-radius:50%;background:rgba(255,51,102,.85)}
.play::after{content:"";position:absolute;left:25px;top:19px;border-left:20px solid #fff;border-top:13px solid transparent;border-bottom:13px solid transparent}
.pager{position:absolute;top:2432px;width:12px;height:12px;border-radius:50%}

.offer{position:absolute;left:0;top:2506px;width:1200px;height:670px;overflow:hidden;
  background:linear-gradient(90deg,#3a28b0 0%,#4a2aa8 45%,#7a2a86 75%,#b03070 100%)}
.offer-photo{position:absolute;left:700px;top:0;width:500px;height:670px;background:radial-gradient(ellipse at 60% 45%,rgba(230,90,120,.75),rgba(90,40,150,0) 70%)}
.offer-body{position:absolute;left:111px;top:58px;width:580px;color:var(--white)}
.offer-body .kicker-left{font-size:24px}
.offer-body h2{font-size:44px;font-weight:700}
.offer-body p{font-size:16.5px;line-height:27.5px;margin-top:27px;font-weight:300}
.offer .btn{left:111px;top:547px;width:153px;height:55px;font-size:17px}

.footer-col h4{font-size:20px;font-weight:500;color:var(--ink)}
.footer-col ul{list-style:none;margin-top:14px}
.footer-col li{font-size:17px;color:var(--text);line-height:32.6px;font-weight:300}
.contact-item{display:flex;gap:10px;font-size:17px;color:var(--text);font-weight:300;line-height:25px}
.rule{position:absolute;left:111px;top:3481px;width:978px;height:1px;background:#ccccd6}
.copyright{position:absolute;left:0;top:3512px;width:1200px;text-align:center;font-size:16px;color:var(--text);font-weight:300}
</style>
</head>
<body>

<header class="site-header">
  <div class="brand" style="left:111px;top:24px">
    <div class="brand-mark"></div>
    <div>
      <div class="brand-name">Lena Marwitz</div>
      <div class="brand-tag">Films for the mindful seekers</div>
    </div>
  </div>
  <nav class="main-nav">
    <a class="active" href="#">Home</a><a href="#">Offer</a><a href="#">References</a><a href="#">About me</a><a href="#">Imprint</a>
  </nav>
</header>

<section class="hero" role="img" aria-label="Filmmaker operating a professional video camera on a rooftop at dusk">
  <h1 class="hero-title">Films for the<br>mindful seekers</h1>
  <a class="btn" href="#">Request an offer</a>
</section>

<section class="process">
  <div class="kicker" style="top:826px">How it works</div>
  <h2 class="heading" style="top:865px">Video Production Process</h2>
  <div class="process-line"></div>
  <div class="dot" style="left:104px"></div>
  <div class="dot" style="left:1075px"></div>

  <div class="step" style="left:101px">
    <div class="step-icon"><svg width="70" height="70" viewBox="0 0 70 70" fill="none" stroke="var(--blue)" stroke-width="2.5" stroke-linecap="round"><rect x="14" y="10" width="42" height="52" rx="3"/><path d="M22 24h26M22 34h26M22 44h16" stroke="var(--pink)"/></svg></div>
    <div class="step-num">Step 1</div>
    <div class="step-name">Conception</div>
    <div class="step-text">Lorem ipsum dolor sitamt<br>consectetur adipsis.</div>
  </div>
  <div class="step" style="left:349px">
    <div class="step-icon"><svg width="70" height="70" viewBox="0 0 70 70" fill="none" stroke="var(--blue)" stroke-width="2.5" stroke-linecap="round" stroke-linejoin="round"><rect x="12" y="14" width="46" height="44" rx="3"/><path d="M12 26h46M24 8v10M46 8v10"/><path d="M25 42l7 7 13-13" stroke="var(--pink)"/></svg></div>
    <div class="step-num">Step 2</div>
    <div class="step-name">Pre-Production</div>
    <div class="step-text">Lorem ipsum dolor sitamt<br>consectetur adipsis.</div>
  </div>
  <div class="step" style="left:598px">
    <div class="step-icon"><svg width="70" height="70" viewBox="0 0 70 70" fill="none" stroke="var(--blue)" stroke-width="2.5" stroke-linejoin="round"><rect x="8" y="22" width="38" height="28" rx="3"/><path d="M46 31l16-8v26l-16-8z" stroke="var(--pink)"/></svg></div>
    <div class="step-num">Step 3</div>
    <div class="step-name">Production</div>
    <div class="step-text">Lorem ipsum dolor sitamt<br>consectetur adipsis.</div>
  </div>
  <div class="step" style="left:847px">
    <div class="step-icon"><svg width="70" height="70" viewBox="0 0 70 70" fill="none" stroke="var(--blue)" stroke-width="2.5" stroke-linecap="round"><rect x="8" y="12" width="54" height="36" rx="3"/><path d="M26 60h18M35 48v12"/><path d="M18 38l10-10 8 6 14-12" stroke="var(--pink)"/></svg></div>
    <div class="step-num">Step 4</div>
    <div class="step-name">Post-Production</div>
    <div class="step-text">Lorem ipsum dolor sitamt<br>consectetur adipsis.</div>
  </div>
</section>

<section class="about">
  <div class="about-photo" role="img" aria-label="Black and white portrait of the filmmaker smiling"></div>
  <div class="about-body">
    <div class="kicker-left">About Me</div>
    <h2>Lena Marwitz</h2>
    <p>My name is Lena and I do movies - with enthusiasm and wholeheartedly. I am a holistic filmmaker.</p>
    <p style="margin-top:27px">At the end of the 1990s, I was faced with the question of whether I should go into alternative medicine or the film industry as a career. Professionally, I chose film at that time, but the spiritual and my passion for the so-called alternative healing methods have accompanied me almost as intensely ever since.</p>
  </div>
  <a class="btn" href="#">Read more</a>
</section>

<section class="work">
  <div class="kicker" style="top:2002px">My Work</div>
  <h2 class="heading" style="top:2039px">Realized projects</h2>
  <div class="thumb" style="left:111px;top:2161px;width:306px;height:204px;background:linear-gradient(120deg,#8a6a5a,#c46a8a)" role="img" aria-label="Video still of a woman speaking in a seminar room"><div class="play"></div></div>
  <div class="thumb" style="left:782px;top:2161px;width:307px;height:204px;background:linear-gradient(120deg,#5a8ac8,#9ab8d8)" role="img" aria-label="Video still of a woman outdoors near a television tower"><div class="play"></div></div>
  <div class="thumb" style="left:1105px;top:2161px;width:95px;height:204px;background:linear-gradient(120deg,#8a8a7a,#c8c8ba)" role="img" aria-label="Video still of a person at a presentation"></div>
  <div class="thumb" style="left:417px;top:2136px;width:365px;height:254px;background:linear-gradient(120deg,#4a4a3a,#8a5a4a 55%,#c84a5a)" role="img" aria-label="Video still of two people at a healing session"><div class="play"></div></div>
  <div class="pager" style="left:585px;background:var(--blue)"></div>
  <div class="pager" style="left:603px;background:#ccccdd"></div>
</section>

<section class="offer">
  <div class="offer-photo" role="img" aria-label="Smiling filmmaker in a fur-hooded jacket behind a camera lens"></div>
  <div class="offer-body">
    <div class="kicker-left">Services</div>
    <h2>My Offer</h2>
    <p style="margin-top:32px">Making a movie is always a journey to yourself. With simple means and without special effects, I accompany you on the way to portraying your essence. A documentary commercial film close to the people. My work is aimed at all people and institutions whose striving for truthfulness is the driving force behind their actions.</p>
    <p>High-quality image design and the informative and comprehensible communication of complex issues are the passion and basis of my image films and company presentations.</p>
    <p>As a full-service provider, I offer everything from one source, from consulting and conception to the finished film.</p>
  </div>
  <a class="btn" href="#">Read more</a>
</section>

<footer>
  <div class="brand" style="left:111px;top:3243px">
    <div class="brand-mark"></div>
    <div>
      <div class="brand-name">Lena Marwitz</div>
      <div class="brand-tag">Films for the mindful seekers</div>
    </div>
  </div>
  <div class="footer-col abs" style="left:575px;top:3243px">
    <h4>Quick Links</h4>
    <ul><li>Home</li><li>Offer</li><li>References</li><li>About me</li><li>Imprint</li></ul>
  </div>
  <div class="footer-col abs" style="left:772px;top:3243px">
    <h4>Contact</h4>
    <div class="contact-item" style="margin-top:20px"><svg width="12" height="20" viewBox="0 0 12 20" style="margin-top:3px"><path d="M6 0a6 6 0 0 0-6 6c0 5 6 12 6 12s6-7 6-12a6 6 0 0 0-6-6zm0 8.5a2.5 2.5 0 1 1 0-5 2.5 2.5 0 0 1 0 5z" fill="var(--pink)"/></svg><span>Lindenweg 14<br>80331 Munich</span></div>
    <div class="contact-item" style="margin-top:24px"><svg width="14" height="14" viewBox="0 0 24 24" style="margin-top:5px"><path d="M6.6 10.8a15 15 0 0 0 6.6 6.6l2.2-2.2c.3-.3.7-.4 1-.2 1.1.4 2.3.6 3.6.6.6 0 1 .4 1 1V20c0 .6-.4 1-1 1A17 17 0 0 1 3 4c0-.6.4-1 1-1h3.5c.6 0 1 .4 1 1 0 1.3.2 2.5.6 3.6.1.3 0 .7-.2 1z" fill="var(--pink)"/></svg><span>1 555 010 2040</span></div>
    <div class="contact-item" style="margin-top:24px"><svg width="16" height="12" viewBox="0 0 16 12" style="margin-top:7px"><rect width="16" height="12" rx="1.5" fill="var(--pink)"/><path d="M1 1l7 5 7-5" stroke="#fff" stroke-width="1.4" fill="none"/></svg><span>info@lenamarwitz.com</span></div>
  </div>
  <div class="rule"></div>
  <div class="copyright">Copyright © 2023, Lena Marwitz. All rights reserved.</div>
</footer>

</body>
</html>
```